Patent Law

Need to develop a home page for a patent lawyer.

Colors should go with logo, blues...

Company Name- Corvel Tindry, PLLC

Company Overview-

I am an Intellectual Property Lawyer and focus on patents, copyrights, trademarks, & trade secrets. I work with small businesses and start ups in the chemical and biotech industries.

Why Us-

I am small firm that can provide large-firm service at a reasonable price. I also can charge flat-fees for entreprenuers in certain practice areas.

Services-
Intellectual Property
Patents
Copyrights
Trademarks
Trade secrets
Healthcare Compliance
Elder law
Wills
Trusts

Website we like-
http://www.quarnlowtide.example/ - within industry!!
http://www.vopperhask.example/
http://dulbrickovan.example/
http://thefernwoldguides.example/

Target Market(s)

My customers will be small business, specifically small start-up companies in the chemical and biotech arena.

Industry/Entity Type

Trade

Requirements
Must have
• Colors should go with logo, blues...

```html
<!DOCTYPE html>
<html lang="en">
<head>
<meta charset="utf-8">
<title>Corvel Tindry, PLLC — Intellectual Property Law</title>
<link rel="stylesheet" href="https://fonts.googleapis.com/css2?family=Open+Sans:wght@400;600&family=Cinzel:wght@400&family=Tinos&display=swap">
<style>
:root{
  --blue:#0a6fb5;
  --blue-dark:#0560a3;
  --blue-footer-top:#0a86c4;
  --blue-footer-bot:#0467ac;
  --blue-bar:#0563a8;
  --ink:#3d3d3d;
  --muted:#777;
  --rule:#d4d4d4;
  --link-light:#d6ecfa;
}
*{margin:0;padding:0;box-sizing:border-box}
html,body{width:1075px;height:1200px;overflow:hidden;background:#fff}
body{position:relative;font-family:"Open Sans",Arial,sans-serif;color:var(--ink)}

/* Header */
.site-header{position:absolute;left:0;top:0;width:1075px;height:109px;border-bottom:1px solid var(--rule)}
.brand{position:absolute;left:62px;top:52px;display:flex;align-items:center;gap:10px}
.brand-dot{width:22px;height:22px;border-radius:50%;background:var(--blue)}
.brand-name{font-size:20px;color:#555;letter-spacing:.5px;text-transform:uppercase;font-weight:400}
.top-contact{position:absolute;right:30px;top:12px;display:flex;align-items:center;gap:8px;color:var(--blue)}
.top-contact .phone{font-size:19px}
.top-contact .sep{color:var(--blue);font-size:15px;margin:0 2px}
.top-contact .map{font-size:15px}
.main-nav{position:absolute;right:16px;top:60px;display:flex}
.main-nav a{font-size:15.5px;color:#444;text-decoration:none;padding:0 15px;border-left:1px solid var(--rule);line-height:22px}
.main-nav a:first-child{border-left:none}

/* Hero */
.hero{position:absolute;left:0;top:110px;width:1051px;height:427px;overflow:hidden;
  background:linear-gradient(90deg,#fbfcfd 0%,#f2f5f8 35%,#e7edf2 55%,#dde3e8 100%)}
.hero-photo{position:absolute;left:365px;top:0;width:686px;height:427px;
  background:linear-gradient(90deg,rgba(255,255,255,0) 0%,rgba(214,186,160,.55) 45%,rgba(40,50,70,.55) 75%,rgba(230,235,240,.4) 100%)}
.hero-title-1{position:absolute;left:80px;top:100px;font-family:"Tinos",serif;font-size:35px;color:#6f6f6f}
.hero-title-2{position:absolute;left:79px;top:136px;font-family:"Tinos",serif;font-size:47px;color:var(--blue)}
.hero-copy{position:absolute;left:82px;top:191px;width:380px;font-size:13px;line-height:21px;color:#666}
.hero-dots{position:absolute;left:82px;top:267px;display:flex;gap:3px}
.hero-dots span{width:13px;height:13px;border-radius:50%;background:#bbb}
.hero-dots span:first-child{background:#111}

/* Feature columns */
.features{position:absolute;left:53px;top:555px;width:972px;height:334px;border:1px solid var(--rule);display:flex;
  background:linear-gradient(180deg,#fff 70%,#f4f4f4 100%)}
.feature{flex:1;border-left:1px solid var(--rule);padding:18px 19px 0}
.feature:first-child{border-left:none}
.feature h2{font-family:"Cinzel",serif;font-weight:400;font-size:25px;color:var(--blue);letter-spacing:.5px;margin-bottom:6px}
.feature-media{width:281px;height:112px;margin-left:2px}
.media-team{background:linear-gradient(135deg,#5a3a26,#b8926e 50%,#2f2118)}
.media-justice{background:linear-gradient(180deg,#6f8fb3,#b7c6d6 60%,#47566a)}
.media-map{background:linear-gradient(135deg,#e4dcec,#f2ecd6 50%,#cfe3d6)}
.lead{margin:10px 2px 0;font-size:14.5px;line-height:21px;color:#333}
.body-copy{margin:8px 2px 0;font-size:12.5px;line-height:21px;color:#777}
.services-title{margin:10px 4px 0;font-size:14.5px;color:var(--blue)}
.service-list{display:flex;gap:16px;margin:8px 4px 0}
.service-list ul{list-style:none}
.service-list li{font-size:11.5px;line-height:21px;color:#444;padding-left:11px;position:relative}
.service-list li::before{content:"";position:absolute;left:0;top:7px;border-left:4px solid var(--blue);border-top:4px solid transparent;border-bottom:4px solid transparent}
.contact-note{margin:10px 4px 0;font-size:12px;color:#777}
.contact-firm{margin:8px 4px 0;font-size:14px;color:#444;text-transform:uppercase}
.contact-lines{margin:3px 4px 0;font-size:12px;line-height:22px;color:#666}

/* Footer */
.site-footer{position:absolute;left:0;top:934px;width:1075px;height:214px;
  background:linear-gradient(180deg,var(--blue-footer-top),var(--blue-footer-bot));display:flex;padding:29px 0 0 67px}
.foot-col h3{font-size:15.5px;font-weight:600;color:#fff;margin-bottom:7px}
.foot-col ul{list-style:none}
.foot-col li{font-size:12px;line-height:24.7px;color:var(--link-light)}
.col-1{width:193px}.col-2{width:222px}.col-3{width:200px}.col-4{width:180px}
.social{display:flex;gap:4px;margin-top:9px}
.social span{width:26px;height:26px;border-radius:50%;background:#fff}
.footer-bar{position:absolute;left:0;top:1148px;width:1075px;height:52px;background:var(--blue-bar);
  font-size:11.5px;color:var(--link-light);padding:19px 0 0 72px}
</style>
</head>
<body>

<header class="site-header">
  <div class="brand"><span class="brand-dot"></span><span class="brand-name">Corvel Tindry, PLLC</span></div>
  <div class="top-contact">
    <svg width="16" height="18" viewBox="0 0 16 18" aria-hidden="true"><path d="M4 1 L7 5 L5 7 Q7 11 10 13 L12 11 L15 14 L13 17 Q5 16 1 4 Z" fill="#b0b0b0"/></svg>
    <span class="phone">555.214.0387</span><span class="sep">|</span><span class="map">MAP</span>
  </div>
  <nav class="main-nav">
    <a href="#">HOME</a><a href="#">ABOUT US</a><a href="#">SERVICES</a><a href="#">NEWS</a><a href="#">CAREER</a><a href="#">MEDIA</a><a href="#">CONTACT</a>
  </nav>
</header>

<section class="hero">
  <div class="hero-photo" role="img" aria-label="Photo of a smiling businessman in a suit talking on a mobile phone"></div>
  <p class="hero-title-1">We know the legal</p>
  <p class="hero-title-2">Industry is Changing.</p>
  <p class="hero-copy">Morbi diam mauris, viverra in, gravida eu, mattis in, ante. Morbi eget arcu. Morbi porta, libero id ullamcorper nonummy, nibh ligula pulvinar metus, eget consectetuer</p>
  <div class="hero-dots"><span></span><span></span><span></span></div>
</section>

<section class="features">
  <article class="feature">
    <h2>Why Us</h2>
    <div class="feature-media media-team" role="img" aria-label="Photo of lawyers meeting around a table in a law library"></div>
    <p class="lead">Mauris vel lacus vitae felis vestibulum volutpat. Etiam est nun</p>
    <p class="body-copy">Morbi diam mauris, viverra in, gravida eu, mattis in, ante. Morbi eget arcu. Morbi porta, libero id ullamcorper nonummy, nibh ligula pulvinar metus, eget consectetuer</p>
  </article>
  <article class="feature">
    <h2>What We Do</h2>
    <div class="feature-media media-justice" role="img" aria-label="Photo of a statue of justice holding scales against a blue sky"></div>
    <p class="services-title">Services we provide are:</p>
    <div class="service-list">
      <ul><li>Intellectual Property</li><li>Patents</li><li>Copyrights</li><li>Trademarks</li><li>Trade secrets</li></ul>
      <ul><li>Healthcare Compliance</li><li>Elder law</li><li>Wills</li><li>Trusts</li></ul>
    </div>
  </article>
  <article class="feature">
    <h2>Contact Info</h2>
    <div class="feature-media media-map" role="img" aria-label="Street map showing the office location"></div>
    <p class="contact-note">Duis quam Nam eget lacus Aliquam erat</p>
    <p class="contact-firm">Corvel Tindry, PLLC</p>
    <p class="contact-lines">48 Larkmoor Avenue #3B<br>Brenton 10291 NY<br>Phone no. 555.214.0387<br>Email add. info@corveltindry.example</p>
  </article>
</section>

<footer class="site-footer">
  <div class="foot-col col-1"><h3>QUICK LINKS</h3><ul><li>Duis tincidunt lectus</li><li>Quis dui viverra vestibulum</li><li>Suspendisse vulputate</li><li>Aliquam dui</li><li>Nulla elementum</li></ul></div>
  <div class="foot-col col-2"><h3>SERVICES WE PROVIDE</h3><ul><li>Duis tincidunt lectus</li><li>Quis dui viverra</li><li>Suspendisse vulputate</li><li>Aliquam dui</li><li>Nulla elementum</li></ul></div>
  <div class="foot-col col-3"><h3>ABOUT US</h3><ul><li>Duis tincidunt lectus</li><li>Quis dui viverra vestibulum</li><li>Suspendisse vulputate</li><li>Aliquam dui</li><li>Nulla elementum</li></ul></div>
  <div class="foot-col col-4"><h3>SUPPORT</h3><ul><li>Duis tincidunt lectus</li><li>Quis dui viverra vestibulum</li><li>Suspendisse vulputate</li><li>Aliquam dui</li></ul></div>
  <div class="foot-col"><h3>GET CONNECTED</h3><div class="social"><span></span><span></span><span></span><span></span></div></div>
</footer>
<div class="footer-bar">© 2013 Company Name. All right reserved.&nbsp; Term of Use</div>

</body>
</html>
```